Summer orchestra weekly camp poster BVPE youth orchestra

We are youth orchestra in Texas holds a summer program called: Bright Bow Seasonal Studio (It's for students ages 8-18 who play already play violin/viola/cello/bass in the North Dallas, Texas Area.

We have 2 posters already from Artmarket designers that we have already been using and now are looking for some new designs. (you can see our other two previously purchased designs on the art market website)

The main difference in our camp is that we meet weekly on Saturday for 2 months June and July (not a week or 2 long camp like most music camps). This makes us a better choice locally because you are playing every week for 2 months out if the summer and less likely to lose skills over the summer vacation months.

Poster size: 11" by 17" but needs to be convertible to 8.5 to 11 size as well AND most importantly be in editable format via either Word or Publisher so we can use it every summer and be able to change dates, cost or location as needed.

All the details are below, but on the poster we would need the website listed: www.marlowridgeyouthensemble.example and tell them to go to that website to apply online beginning April 1st

That's how we get business, they go to our website and apply and pay with coinvault. It also needs to say really big BVPE BRIGHT BOW SEASONAL STUDIO

April 1st is when we being accepting online applications (every year, so don't put a year) Also put: Camp is held on Saturdays in June and July with final concert, last Sunday in July

Also on the poster we need: Our goal is to keep young musicians playing over the summer –so don’t put your instrument away for the summer! Keep in shape by joining us for the Marlow Ridge Youth Ensemble’s summer program – Bright Bow Seasonal Studio! Tuition is $225, which covers June/July Saturday rehearsals and the performance fee for the BKMT Hall concert, last Sunday in July.

I know we can't get all the info below on it, but I put it on so you could better understand what we are doing.

We have a logo already, that we have the rights to - I need something that kids/teens will think is cool looking and music related....we are string instruments only (violin, viola, cello, bass) we also want it to look classy looking, not cheap
I included 2 copies of the logo in different color set

here's all the details from our website:
Bright Bow Seasonal Studio (June and July) - Tuition: $225
Somewhere it should stress that we are not like other camps because we are weekly for two months. (There's a better way to state that but I'm not sure what that is)

Rehearsals on Saturdays June &July with final concert on last Sunday in July @ BKH Hall

Our goal is to keep young musicians playing over the summer –so don’t put your instrument away for the summer! Keep in shape by joining us for the Marlow Ridge Youth Ensemble’s new summer program – Bright Bow Seasonal Studio!

Tuition is $225, which covers June/July Saturday rehearsals and the performance fee for the BKMT Hall concert.

No audition is necessary. Enrollment is limited to the first 50 students in each age category, depending on instrumentation needs, so don’t delay – enrollment online begins April 1st. Siblings will receive a $50 discount, after the first child's regular priced tuition.

Bright Bow I: Students entering grades 6 and below (3:00 – 4:20 P.M. )
Bright Bow II: Students grades entering 7 and 8 (4:30 – 6:00 P.M.)
Bright Bow III: Students entering grades 9-12 (6:15 – 7:45 P.M.)

Summer camp attendance policy is more lenient due to summer vacations. Please notify BVPE of summer absences as soon as your vacation/camp dates are known.
Updates

Here is a link to the previous contest we held on ArtMarket last year.

http://jobs.artmarket.example/job.aspx?id=384619

http://poster.artmarket.example/contest.aspx?id=384619

Also Rehearsals are held at Pemberton Fiddles in Allen, TX

I am working today at a music festival and cannot get on the computer or artmarket website until after 6 or 7 p.m. tonight.  So if you are not getting feedback during the day today, that is why.  I will give feedback to everyone when I get home later tonight.  Thank you all for your work!

Reason: Hi everyone, I judged a music contest all day today and really need some time to look over all the entries. I appreciate everyone's hard work and will make a decision within the next 2 days. I want to be able to provide feedback to everyone and give everyone enough time to submit their best work, so I am extending the deadline by 2 days. I will have to make a decision at the end very quickly as we need to do a huge mail out as soon as the contest is over. Thank you everyone, we really do appreciate everyone's efforts in making our new poster for Bright Seasonal Bow Studio!

Target Market(s)

Parents of string players age 8-18 in North Texas along with students themselves.

Industry/Entity Type

Business

Requirements
Must have
• something showing we are different than the ordinary summer music camp
our QR code which I will email to you if your poster is the winner

```html
<!DOCTYPE html>
<html lang="en">
<head>
<meta charset="utf-8">
<title>BVPE Bright Bow Seasonal Studio</title>
<link href="https://fonts.googleapis.com/css2?family=Arimo:ital,wght@1,700&family=Carlito:ital,wght@0,400;0,700;1,400;1,700&family=Patrick+Hand&display=swap" rel="stylesheet">
<style>
  :root {
    --maroon: #7b1f33;
    --maroon-bright: #a3173f;
    --ink: #1d1d1d;
    --rule: #8a8a8a;
    --band-light: #f3f3f1;
    --note-paper: #fbfbf8;
    --goal-box: rgba(150, 150, 150, 0.55);
    --badge: #f4f1e4;
  }
  * { box-sizing: border-box; margin: 0; padding: 0; }
  html, body { width: 777px; height: 1200px; overflow: hidden; background: #fff; }
  .poster {
    position: relative; width: 777px; height: 1200px; overflow: hidden;
    font-family: "Carlito", "Calibri", sans-serif; color: var(--ink);
  }
  .section { position: absolute; left: 0; width: 777px; }

  /* Header */
  .header {
    top: 0; height: 187px;
    border-top: 4px solid var(--rule);
    border-bottom: 3px solid var(--rule);
    background: linear-gradient(100deg, #f2e2ea 0%, #dcefe9 35%, #e3f1e3 60%, #f7f2d6 100%);
  }
  .title {
    font-family: "Arimo", "Arial", sans-serif; font-style: italic; font-weight: 700;
    color: var(--maroon); text-align: center; font-size: 64px; line-height: 92px;
    letter-spacing: 0.5px; padding-top: 0;
    text-shadow: 2px 2px 0 #c9a9b1, 3px 3px 3px rgba(0,0,0,0.35);
  }

  /* Intro */
  .intro {
    top: 187px; height: 277px;
    background: linear-gradient(115deg, #f3f0f0 0%, #d9e5dd 30%, #c6dcd1 55%, #e6ead8 80%, #f5f3df 100%);
  }
  .intro-lead {
    position: absolute; left: 13px; top: 26px; width: 592px;
    font-size: 18px; line-height: 28px; text-align: justify;
  }
  .sticky-note {
    position: absolute; left: 628px; top: 5px; width: 170px; height: 66px;
    background: var(--note-paper); transform: rotate(18deg);
    box-shadow: 1px 2px 4px rgba(0,0,0,0.3);
    font-family: "Patrick Hand", cursive; font-size: 15px; line-height: 20px;
    padding: 10px 0 0 18px; color: #333;
  }
  .difference { position: absolute; left: 25px; top: 132px; width: 700px; }
  .difference h3 { font-size: 17px; font-style: italic; font-weight: 700; margin: 0 0 10px 13px; }
  .difference ul { list-style: none; font-size: 18px; line-height: 29px; }
  .difference li { position: relative; padding-left: 20px; text-align: justify; }
  .difference li::before { content: "\270E"; position: absolute; left: 2px; top: 0; font-size: 14px; }
  .difference strong { font-weight: 700; }

  /* Apply band */
  .apply {
    top: 464px; height: 218px; text-align: center;
    border-top: 2px solid #ddd; border-bottom: 3px solid var(--rule);
    background: linear-gradient(180deg, #fafafa 0%, var(--band-light) 50%, #e6e6e4 100%);
  }
  .apply-heading { margin-top: 10px; font-size: 45px; line-height: 46px; font-weight: 400; color: var(--maroon-bright); letter-spacing: 1px; }
  .apply-note { margin-top: 22px; font-size: 19px; line-height: 23px; font-style: italic; }
  .apply-note sup { font-size: 11px; }
  .apply-date { margin-top: 17px; font-size: 25px; line-height: 30px; }
  .apply-url {
    margin-top: 27px; font-size: 31px; line-height: 36px; font-weight: 700; color: #111;
    text-shadow: 2px 2px 3px rgba(0,0,0,0.35);
  }

  /* Tuition */
  .tuition {
    top: 682px; height: 518px;
    background: linear-gradient(120deg, #f6cfd3 0%, #e4ecdf 35%, #c8ede6 60%, #d7f0c5 85%, #f2f4d4 100%);
  }
  .score-art {
    position: absolute; left: 0; top: 100px; width: 777px; height: 380px;
    background: radial-gradient(ellipse at 40% 55%, rgba(120,200,210,0.45), rgba(255,255,255,0) 70%);
  }
  .tuition-fee { position: absolute; left: 0; width: 777px; top: 20px; line-height: 52px; text-align: center; font-size: 44px; font-weight: 700; letter-spacing: 0.5px; }
  .limit-note { position: absolute; right: 6px; top: 79px; font-size: 14px; font-style: italic; }
  .fee-includes { position: absolute; left: 19px; top: 117px; width: 440px; }
  .fee-includes h4 { font-size: 17px; line-height: 20px; font-weight: 700; text-decoration: underline; margin-bottom: 10px; }
  .fee-includes ul { list-style: none; font-size: 18px; font-weight: 700; line-height: 29px; }
  .fee-includes li::before { content: "\2022"; margin-right: 3px; }
  .fee-includes .venue { display: block; font-weight: 400; font-style: italic; font-size: 17px; line-height: 29px; padding-left: 10px; }

  .goal-box {
    position: absolute; left: 468px; top: 131px; width: 289px; height: 330px;
    background: var(--goal-box); padding: 3px 8px; font-size: 19.5px; line-height: 30px; text-align: justify;
  }
  .goal-box p + p { margin-top: 14px; }
  .goal-box strong { font-weight: 700; }
  .goal-box em { font-weight: 700; font-style: italic; }

  .ensemble-mark {
    position: absolute; left: 120px; top: 360px;
    font-size: 56px; font-weight: 700; color: rgba(120,120,120,0.55); letter-spacing: 6px;
  }
  .pay-badge {
    position: absolute; left: 26px; top: 440px; width: 62px; height: 40px;
    background: var(--badge); border: 1px solid #c9c3a8; border-radius: 4px;
    font-size: 12px; font-weight: 700; color: #2a3b6b; text-align: center; line-height: 38px;
  }
  .footer { position: absolute; left: 0; width: 777px; top: 486px; text-align: center; font-size: 15px; font-style: italic; }
  .footer span { font-style: normal; font-weight: 700; margin-left: 6px; }
</style>
</head>
<body>
<main class="poster">
  <header class="section header">
    <h1 class="title">BVPE BRIGHT BOW<br>SEASONAL STUDIO</h1>
  </header>

  <section class="section intro">
    <p class="intro-lead">Bright Bow Seasonal Studio taking place Saturdays during June &amp; July with a Final Concert held on the last Sunday in July.</p>
    <div class="sticky-note">No Auditions Necessary<br>Siblings get $50 off</div>
    <div class="difference">
      <h3>We Are Different To The Rest</h3>
      <ul>
        <li>Runs on Saturdays for a period of <strong>2 months</strong>, making it a better choice locally;</li>
        <li>Gives you the opportunity to <strong>play every week</strong> for a <strong>full 2 months</strong> over summer vacation time; making you less likely to lose skills.</li>
      </ul>
    </div>
  </section>

  <section class="section apply">
    <h2 class="apply-heading">GO ONLINE TO APPLY</h2>
    <p class="apply-note">Visit our site to apply and submit your application to secure your space<sup>*</sup></p>
    <p class="apply-date">Applications Open 1 April</p>
    <p class="apply-url">www.marlowridgeyouthensemble.example</p>
  </section>

  <section class="section tuition">
    <div class="score-art" role="img" aria-label="Soft swirl of sheet music staves and notes in teal and green"></div>
    <h2 class="tuition-fee">TUITION FEE: $225</h2>
    <p class="limit-note">*Limited to 50 Entrants Per Age category</p>
    <div class="fee-includes">
      <h4>Fee Includes :-</h4>
      <ul>
        <li>All rehearsals on Saturdays for June &amp; July</li>
        <li>Performance Fee <span class="venue">(BKMT Hall Concert - Last Sunday of July)</span></li>
      </ul>
    </div>
    <div class="goal-box">
      <p><strong>Our goal</strong> is to <strong>keep young musicians playing</strong> over the summer time; so don’t put your instrument away <strong>this summer!</strong></p>
      <p><strong>Keep in shape</strong> by joining us for the <strong>Marlow Ridge Youth Ensemble’s</strong> New Summer Program:<br><em>Bright Bow Seasonal Studio</em></p>
    </div>
    <div class="ensemble-mark">BVPE</div>
    <div class="pay-badge">CoinVault</div>
    <p class="footer">For more information, rehearsal times and online applications<span>www.marlowridgeyouthensemble.example</span></p>
  </section>
</main>
</body>
</html>
```